PowerPoint Design for upcoming Broadcast

I need a PowerPoint design complete with all the templates in PPT, i.e two columns of text, one column of text with adjacent area for image, etc. Per the attached logo. Do not use the gold element in the design. 16x9

Target Market(s)

Business Leaders

Industry/Entity Type

Business Consultant

Font styles to use
Other font styles liked:
• Arial

Colors

Designer to choose colors to be used in the design.

Requirements
Must have
• Crisp clean design. #for each color used.
Nice to have
• An assortment of charts in the ppt color schemes. A military (KDFR) theme.
Should not have
• Gaudy. Flashy. Transitions.

```html
<!DOCTYPE html>
<html lang="en">
<head>
<meta charset="utf-8">
<title>KDFR Leadership Presentation Template</title>
<link href="https://fonts.googleapis.com/css2?family=Arimo:wght@400;700&display=swap" rel="stylesheet">
<style>
:root{
  --red:#d3261d;
  --red-mid:#b91c1c;
  --red-light:#e2452f;
  --red-deep:#a3151a;
  --ink:#231f20;
  --stage:#f1f1f1;
  --board:#5a5a5a;
  --paper:#ffffff;
  --paper-warm:#f6f4f1;
  --track:#f3ebe4;
  --muted:#555555;
}
*{margin:0;padding:0;box-sizing:border-box}
html,body{width:1200px;height:2643px;overflow:hidden}
body{background:var(--board);font-family:"Arimo",Arial,sans-serif;position:relative}
.hero{position:absolute;left:0;top:0;width:1200px;height:802px;background:var(--stage)}
.hero .slide{left:240px;top:198px;width:720px;height:405px;box-shadow:0 18px 40px rgba(0,0,0,.18)}
.slide{position:absolute;width:543px;height:305px;background:var(--paper);overflow:hidden;box-shadow:0 10px 22px rgba(0,0,0,.35)}
.slide svg{display:block;width:100%;height:100%}
.col-l{left:48px}.col-r{left:631px}
.row-1{top:863px}.row-2{top:1221px}.row-3{top:1575px}.row-4{top:1929px}.row-5{top:2285px}
svg text{font-family:"Arimo",Arial,sans-serif}
.t-title{font-weight:700;font-size:20px;fill:var(--ink)}
.t-accent{fill:var(--red)}
.t-white{fill:#fff}
.t-body{font-size:5.6px;fill:var(--muted)}
.t-body-w{font-size:5.6px;fill:#fff}
.t-foot{font-size:5px;fill:#444}
.t-list{font-size:7px;fill:#333}
.t-num{font-size:7.5px;font-weight:700;fill:#fff}
.t-label{font-size:7.5px;font-weight:700;fill:#fff}
.brand{font-weight:700;fill:#fff}
</style>
</head>
<body>

<section class="hero">
  <div class="slide">
    <svg viewBox="0 0 543 305">
      <rect x="0" y="0" width="543" height="305" fill="var(--ink)"/>
      <rect x="0" y="110" width="543" height="195" fill="#9a9a9a" role="img" aria-label="Grayscale photo of soldiers with armoured vehicle"/>
      <polygon points="0,0 543,0 543,95 272,152 0,95" fill="var(--ink)"/>
      <polygon points="0,95 272,152 543,95 543,110 272,167 0,110" fill="var(--red)"/>
      <polygon points="222,0 322,0 322,26 272,34 222,26" fill="var(--red)"/>
      <text x="272" y="22" text-anchor="middle" class="t-white" font-size="17" font-weight="700">2018</text>
      <text x="272" y="76" text-anchor="middle" class="t-white" font-size="25" font-weight="700">PRESENTATION TITLE GOES HERE</text>
      <circle cx="272" cy="152" r="44" fill="var(--red)"/>
      <text x="272" y="160" text-anchor="middle" class="brand" font-size="22">KDFR</text>
    </svg>
  </div>
</section>

<div class="slide col-l row-1">
  <svg viewBox="0 0 543 305">
    <rect x="0" y="0" width="543" height="305" fill="var(--ink)"/>
    <rect x="0" y="110" width="543" height="195" fill="#9a9a9a" role="img" aria-label="Grayscale photo of soldiers with armoured vehicle"/>
    <polygon points="0,0 543,0 543,95 272,152 0,95" fill="var(--ink)"/>
    <polygon points="0,95 272,152 543,95 543,110 272,167 0,110" fill="var(--red)"/>
    <polygon points="222,0 322,0 322,26 272,34 222,26" fill="var(--red)"/>
    <text x="272" y="22" text-anchor="middle" class="t-white" font-size="17" font-weight="700">2018</text>
    <text x="272" y="76" text-anchor="middle" class="t-white" font-size="25" font-weight="700">PRESENTATION TITLE GOES HERE</text>
    <circle cx="272" cy="152" r="44" fill="var(--red)"/>
    <text x="272" y="160" text-anchor="middle" class="brand" font-size="22">KDFR</text>
  </svg>
</div>

<div class="slide col-r row-1">
  <svg viewBox="0 0 543 305">
    <polygon points="0,0 185,0 218,152 185,305 0,305" fill="#6f7a5a" role="img" aria-label="Photo of a veteran holding a national flag"/>
    <polygon points="190,0 206,0 240,152 206,305 190,305 224,152" fill="var(--ink)"/>
    <circle cx="312" cy="65" r="10" fill="var(--red)"/><text x="312" y="68" text-anchor="middle" class="t-num">01</text>
    <text x="340" y="68" class="t-list">LOREM IPSUM SIMPLY TEXT</text>
    <circle cx="312" cy="107" r="10" fill="var(--red)"/><text x="312" y="110" text-anchor="middle" class="t-num">02</text>
    <text x="340" y="110" class="t-list">LOREM IPSUM SIMPLY TEXT</text>
    <circle cx="312" cy="150" r="10" fill="var(--red)"/><text x="312" y="153" text-anchor="middle" class="t-num">03</text>
    <text x="340" y="153" class="t-list">LOREM IPSUM SIMPLY TEXT</text>
    <circle cx="312" cy="192" r="10" fill="var(--red)"/><text x="312" y="195" text-anchor="middle" class="t-num">04</text>
    <text x="340" y="195" class="t-list">LOREM IPSUM SIMPLY TEXT</text>
    <circle cx="312" cy="234" r="10" fill="var(--red)"/><text x="312" y="237" text-anchor="middle" class="t-num">05</text>
    <text x="340" y="237" class="t-list">LOREM IPSUM SIMPLY TEXT</text>
    <text x="272" y="296" text-anchor="middle" class="t-foot">www.ipsumsite.com</text>
    <text x="530" y="296" text-anchor="end" class="t-foot">01</text>
  </svg>
</div>

<div class="slide col-l row-2">
  <svg viewBox="0 0 543 305">
    <rect width="543" height="305" fill="var(--paper-warm)"/>
    <rect x="0" y="0" width="543" height="305" fill="#eeebe7" opacity=".6" role="img" aria-label="Faint photo of soldiers in the field"/>
    <polygon points="113,0 430,0 430,100 272,122 113,100" fill="var(--ink)"/>
    <polygon points="113,100 272,122 430,100 430,110 272,132 113,110" fill="var(--red)"/>
    <circle cx="272" cy="54" r="16" fill="var(--red)" stroke="#fff" stroke-width="2"/>
    <text x="272" y="58" text-anchor="middle" class="t-white" font-size="11" font-weight="700">01</text>
    <text x="272" y="182" text-anchor="middle" class="t-title">LOREM IPSUM <tspan class="t-accent">SIMPLY TEXT</tspan></text>
    <text x="272" y="196" text-anchor="middle" class="t-body">Lorem Ipsum is simply dummy text of the printing and typesetting industry. Lorem</text>
    <text x="272" y="204" text-anchor="middle" class="t-body">Ipsum has been the industry's standard dummy text ever since the 1500s.</text>
    <circle cx="272" cy="232" r="9" fill="var(--red)"/>
    <path d="M272 227v9M268 232.5l4 4 4-4" stroke="#fff" stroke-width="1.6" fill="none"/>
    <text x="272" y="296" text-anchor="middle" class="t-foot">www.ipsumsite.com</text>
    <text x="530" y="296" text-anchor="end" class="t-foot">02</text>
  </svg>
</div>

<div class="slide col-r row-2">
  <svg viewBox="0 0 543 305">
    <text x="272" y="28" text-anchor="middle" class="t-title">LOREM IPSUM <tspan class="t-accent">SIMPLY TEXT</tspan></text>
    <rect x="0" y="108" width="543" height="106" fill="var(--ink)"/>
    <rect x="16" y="70" width="164" height="182" fill="#5b5a48" role="img" aria-label="Photo of a saluting officer in dress uniform"/>
    <text x="198" y="130" class="t-body-w">Lorem Ipsum is simply dummy text of the printing and typesetting industry. Lorem</text>
    <text x="198" y="141" class="t-body-w">Ipsum has been the industry's standard dummy text ever since the 1500s, when an</text>
    <text x="198" y="152" class="t-body-w">unknown printer took a galley of type and scrambled it to make a type specimen</text>
    <text x="198" y="163" class="t-body-w">book. It has survived not only five centuries, but also the leap into electronic</text>
    <text x="198" y="174" class="t-body-w">typesetting, remaining essentially unchanged.</text>
    <text x="272" y="296" text-anchor="middle" class="t-foot">www.ipsumsite.com</text>
    <text x="530" y="296" text-anchor="end" class="t-foot">03</text>
  </svg>
</div>

<div class="slide col-l row-3">
  <svg viewBox="0 0 543 305">
    <text x="272" y="28" text-anchor="middle" class="t-title">LOREM IPSUM <tspan class="t-accent">SIMPLY TEXT</tspan></text>
    <g>
      <circle cx="74" cy="128" r="42" fill="none" stroke="var(--red-deep)" stroke-width="18"/>
      <circle cx="74" cy="128" r="42" fill="none" stroke="var(--red)" stroke-width="18" stroke-dasharray="175 89"/>
      <circle cx="74" cy="128" r="15" fill="var(--ink)"/>
      <circle cx="74" cy="123" r="4" fill="#fff"/><path d="M66 136q8-10 16 0z" fill="#fff"/>
    </g>
    <g>
      <circle cx="271" cy="128" r="42" fill="none" stroke="var(--red-deep)" stroke-width="18"/>
      <circle cx="271" cy="128" r="42" fill="none" stroke="var(--red)" stroke-width="18" stroke-dasharray="200 64"/>
      <circle cx="271" cy="128" r="15" fill="var(--ink)"/>
      <circle cx="271" cy="123" r="4" fill="#fff"/><path d="M263 136q8-10 16 0z" fill="#fff"/>
    </g>
    <g>
      <circle cx="469" cy="128" r="42" fill="none" stroke="var(--red-deep)" stroke-width="18"/>
      <circle cx="469" cy="128" r="42" fill="none" stroke="var(--red)" stroke-width="18" stroke-dasharray="150 114"/>
      <circle cx="469" cy="128" r="15" fill="var(--ink)"/>
      <circle cx="469" cy="123" r="4" fill="#fff"/><path d="M461 136q8-10 16 0z" fill="#fff"/>
    </g>
    <g class="t-body" text-anchor="middle">
      <text x="74" y="206">Lorem Ipsum is simply</text><text x="74" y="215">dummy text of the printing</text><text x="74" y="224">and typesetting industry.</text>
      <text x="271" y="206">Lorem Ipsum is simply</text><text x="271" y="215">dummy text of the printing</text><text x="271" y="224">and typesetting industry.</text>
      <text x="469" y="206">Lorem Ipsum is simply</text><text x="469" y="215">dummy text of the printing</text><text x="469" y="224">and typesetting industry.</text>
    </g>
    <text x="272" y="296" text-anchor="middle" class="t-foot">www.ipsumsite.com</text>
    <text x="530" y="296" text-anchor="end" class="t-foot">04</text>
  </svg>
</div>

<div class="slide col-r row-3">
  <svg viewBox="0 0 543 305">
    <text x="272" y="28" text-anchor="middle" class="t-title">LOREM IPSUM <tspan class="t-accent">SIMPLY TEXT</tspan></text>
    <g stroke="var(--red-deep)" stroke-width="1.5" fill="none">
      <polyline points="382,83 448,83 448,118"/>
      <line x1="340" y1="166" x2="408" y2="166"/>
      <polyline points="418,245 500,245 500,205"/>
    </g>
    <circle cx="458" cy="160" r="50" fill="var(--red-deep)"/>
    <circle cx="458" cy="160" r="38" fill="var(--red)"/>
    <text x="458" y="166" text-anchor="middle" class="brand" font-size="16">KDFR</text>
    <rect x="294" y="74" width="88" height="18" fill="var(--red-deep)"/>
    <text x="338" y="86" text-anchor="middle" class="t-label">LOREM IPSUM</text>
    <rect x="246" y="157" width="94" height="18" fill="var(--red)"/>
    <text x="293" y="169" text-anchor="middle" class="t-label">LOREM IPSUM</text>
    <rect x="324" y="236" width="94" height="18" fill="var(--red)"/>
    <text x="371" y="248" text-anchor="middle" class="t-label">LOREM IPSUM</text>
    <text x="282" y="80" text-anchor="end" class="t-body">Lorem Ipsum is simply dummy text of the</text>
    <text x="282" y="89" text-anchor="end" class="t-body">printing and typesetting industry Lorem Ipsum.</text>
    <text x="234" y="163" text-anchor="end" class="t-body">Lorem Ipsum is simply dummy text of the</text>
    <text x="234" y="172" text-anchor="end" class="t-body">printing and typesetting industry Lorem Ipsum.</text>
    <text x="312" y="242" text-anchor="end" class="t-body">Lorem Ipsum is simply dummy text of the</text>
    <text x="312" y="251" text-anchor="end" class="t-body">printing and typesetting industry Lorem Ipsum.</text>
    <text x="272" y="296" text-anchor="middle" class="t-foot">www.ipsumsite.com</text>
    <text x="530" y="296" text-anchor="end" class="t-foot">05</text>
  </svg>
</div>

<div class="slide col-l row-4">
  <svg viewBox="0 0 543 305">
    <rect width="543" height="305" fill="var(--paper-warm)"/>
    <rect x="0" y="0" width="543" height="305" fill="#e4e1dd" opacity=".6" role="img" aria-label="Faint photo of soldiers advancing"/>
    <polygon points="113,0 430,0 430,100 272,122 113,100" fill="var(--ink)"/>
    <polygon points="113,100 272,122 430,100 430,110 272,132 113,110" fill="var(--red)"/>
    <circle cx="272" cy="54" r="16" fill="var(--red)" stroke="#fff" stroke-width="2"/>
    <text x="272" y="58" text-anchor="middle" class="t-white" font-size="11" font-weight="700">02</text>
    <text x="272" y="182" text-anchor="middle" class="t-title">LOREM IPSUM <tspan class="t-accent">SIMPLY TEXT</tspan></text>
    <text x="272" y="196" text-anchor="middle" class="t-body">Lorem Ipsum is simply dummy text of the printing and typesetting industry. Lorem</text>
    <text x="272" y="204" text-anchor="middle" class="t-body">Ipsum has been the industry's standard dummy text ever since the 1500s.</text>
    <circle cx="272" cy="232" r="9" fill="var(--red)"/>
    <path d="M272 227v9M268 232.5l4 4 4-4" stroke="#fff" stroke-width="1.6" fill="none"/>
    <text x="272" y="296" text-anchor="middle" class="t-foot">www.ipsumsite.com</text>
    <text x="530" y="296" text-anchor="end" class="t-foot">06</text>
  </svg>
</div>

<div class="slide col-r row-4">
  <svg viewBox="0 0 543 305">
    <text x="272" y="28" text-anchor="middle" class="t-title">LOREM IPSUM <tspan class="t-accent">SIMPLY TEXT</tspan></text>
    <polygon points="10,102 130,102 146,130 130,158 10,158" fill="var(--red-light)"/>
    <polygon points="136,102 256,102 272,130 256,158 136,158 152,130" fill="var(--red)"/>
    <polygon points="262,102 382,102 398,130 382,158 262,158 278,130" fill="var(--red-mid)"/>
    <polygon points="388,102 508,102 524,130 508,158 388,158 404,130" fill="var(--red-deep)"/>
    <g fill="var(--ink)" stroke="#fff" stroke-width="2">
      <circle cx="30" cy="130" r="14"/><circle cx="156" cy="130" r="14"/>
      <circle cx="282" cy="130" r="14"/><circle cx="408" cy="130" r="14"/>
    </g>
    <g class="t-white" font-size="12" font-weight="700" text-anchor="middle">
      <text x="30" y="134">A</text><text x="156" y="134">B</text>
      <text x="282" y="134">C</text><text x="408" y="134">D</text>
    </g>
    <g fill="#fff">
      <circle cx="82" cy="124" r="5"/><path d="M72 142q10-14 20 0z"/>
      <circle cx="208" cy="124" r="5"/><path d="M198 142q10-14 20 0z"/>
      <circle cx="334" cy="124" r="5"/><path d="M324 142q10-14 20 0z"/>
      <circle cx="460" cy="124" r="5"/><path d="M450 142q10-14 20 0z"/>
    </g>
    <g class="t-body" text-anchor="middle">
      <text x="70" y="178">Lorem Ipsum is simply dummy</text><text x="70" y="187">text of the printing and</text><text x="70" y="196">typesetting industry.</text>
      <text x="198" y="178">Lorem Ipsum is simply dummy</text><text x="198" y="187">text of the printing and</text><text x="198" y="196">typesetting industry.</text>
      <text x="326" y="178">Lorem Ipsum is simply dummy</text><text x="326" y="187">text of the printing and</text><text x="326" y="196">typesetting industry.</text>
      <text x="454" y="178">Lorem Ipsum is simply dummy</text><text x="454" y="187">text of the printing and</text><text x="454" y="196">typesetting industry.</text>
    </g>
    <text x="272" y="296" text-anchor="middle" class="t-foot">www.ipsumsite.com</text>
    <text x="530" y="296" text-anchor="end" class="t-foot">07</text>
  </svg>
</div>

<div class="slide col-l row-5">
  <svg viewBox="0 0 543 305">
    <text x="272" y="28" text-anchor="middle" class="t-title">LOREM IPSUM <tspan class="t-accent">SIMPLY TEXT</tspan></text>
    <rect x="14" y="86" width="200" height="70" fill="#8a8f96" role="img" aria-label="Photo of business people working at a desk with a laptop"/>
    <rect x="14" y="166" width="200" height="12" fill="var(--red)"/>
    <text x="114" y="174.5" text-anchor="middle" class="t-white" font-size="6" font-weight="700">LOREM IPSUM IS SIMPLY DUMMY TEXT</text>
    <rect x="14" y="182" width="200" height="40" fill="var(--paper-warm)"/>
    <text x="114" y="194" text-anchor="middle" class="t-body">Lorem Ipsum is simply dummy text of the printing and</text>
    <text x="114" y="203" text-anchor="middle" class="t-body">typesetting industry. Lorem Ipsum has been the</text>
    <text x="114" y="212" text-anchor="middle" class="t-body">industry's standard dummy text ever since the 1500s.</text>
    <g>
      <rect x="258" y="101" width="240" height="10" rx="5" fill="var(--track)"/>
      <rect x="258" y="101" width="60" height="10" rx="5" fill="var(--red)"/>
      <rect x="503" y="100" width="27" height="12" fill="var(--red)"/>
      <text x="516.5" y="109" text-anchor="middle" class="t-num">30</text>
      <rect x="258" y="139" width="240" height="10" rx="5" fill="var(--track)"/>
      <rect x="258" y="139" width="190" height="10" rx="5" fill="var(--red)"/>
      <rect x="503" y="138" width="27" height="12" fill="var(--red)"/>
      <text x="516.5" y="147" text-anchor="middle" class="t-num">85</text>
      <rect x="258" y="175" width="240" height="10" rx="5" fill="var(--track)"/>
      <rect x="258" y="175" width="34" height="10" rx="5" fill="var(--red-mid)"/>
      <rect x="503" y="174" width="27" height="12" fill="var(--red-mid)"/>
      <text x="516.5" y="183" text-anchor="middle" class="t-num">20</text>
      <rect x="258" y="213" width="240" height="10" rx="5" fill="var(--track)"/>
      <rect x="258" y="213" width="48" height="10" rx="5" fill="var(--red-deep)"/>
      <rect x="503" y="212" width="27" height="12" fill="var(--red-deep)"/>
      <text x="516.5" y="221" text-anchor="middle" class="t-num">29</text>
    </g>
    <text x="272" y="296" text-anchor="middle" class="t-foot">www.ipsumsite.com</text>
    <text x="530" y="296" text-anchor="end" class="t-foot">08</text>
  </svg>
</div>

<div class="slide col-r row-5">
  <svg viewBox="0 0 543 305">
    <rect width="543" height="305" fill="var(--ink)"/>
    <rect x="0" y="70" width="543" height="180" fill="#ededed" role="img" aria-label="Faint photo of a military parade"/>
    <polygon points="0,52 272,140 543,52 543,70 272,158 0,70" fill="var(--red)"/>
    <polygon points="0,232 272,140 543,232 543,250 272,158 0,250" fill="var(--red)"/>
    <polygon points="0,0 543,0 543,52 272,140 0,52" fill="var(--ink)"/>
    <polygon points="0,250 272,158 543,250 543,305 0,305" fill="var(--ink)"/>
    <text x="272" y="50" text-anchor="middle" class="t-white" font-size="20" font-weight="700">THANK YOU</text>
    <circle cx="272" cy="148" r="42" fill="var(--red)"/>
    <text x="272" y="156" text-anchor="middle" class="brand" font-size="22">KDFR</text>
    <text x="272" y="240" text-anchor="middle" class="t-white" font-size="12" font-weight="700">CONTACT US</text>
    <g class="t-white" font-size="6">
      <circle cx="36" cy="276" r="3" fill="#fff"/><text x="43" y="278">Address Goes Here</text>
      <circle cx="168" cy="276" r="3" fill="#fff"/><text x="175" y="278">Phone No. Goes Here</text>
      <rect x="295" y="273" width="7" height="5" fill="#fff"/><text x="306" y="278">Email Goes Here</text>
      <circle cx="412" cy="276" r="3" fill="#fff"/><text x="419" y="278">Web Address Goes Here</text>
    </g>
  </svg>
</div>

</body>
</html>
```